Unique Disposable facemask 50counts box

We need a new unique modern contemporaries design for disposable face mask . It made in USA. Different from just regular face mask box. Maybe shoe box design style or cigarette box design.
Updates

Low designer entries

Still waiting for the box structure templates. Hope the box printing company finishes the final dimensions and final style of the box structures this week

Designs look the same

Target Market(s)

USA 🇺🇸 market

Colors
f37122
ec1f27
00a990

Requirements
Must have
• Made in USA logo. Contemporar color schemes. (Attachment images)
Nice to have
• Diagram of the mask, usage instructions, UPC code, lot# and exp date location,
Should not have
• People with mask images

```html
<!DOCTYPE html>
<html lang="en">
<head>
<meta charset="utf-8">
<title>Disposable Face Mask – Box Front</title>
<link href="https://fonts.googleapis.com/css2?family=Barlow+Condensed:ital,wght@0,600;1,600&family=Archivo+Black&display=swap" rel="stylesheet">
<style>
  :root {
    --backdrop: #3c414d;
    --box-dark: #1f3035;
    --box-edge: #172428;
    --pattern-deep: #3f6d80;
    --pattern-light: #9fb9c8;
    --panel-bg: #e2e3e4;
    --panel-frame: #5a7dbd;
    --band-dark: #2a3a3f;
    --title-light: #7bbcdc;
    --title-deep: #4a7d99;
    --mask-fill: #c9dfe9;
    --badge-red: #b3303b;
    --badge-blue: #2e4f8a;
    --logo-text: #e6e9ea;
  }
  * { margin: 0; padding: 0; box-sizing: border-box; }
  html, body {
    width: 1200px; height: 960px; overflow: hidden;
    background: var(--backdrop);
  }
  .box-front {
    position: absolute; left: 80px; top: 160px;
    width: 1040px; height: 640px;
    background: var(--box-dark);
    border: 2px solid var(--box-edge);
  }
  .brand-spine {
    position: absolute; left: 0; top: 0; width: 170px; height: 100%;
    display: flex; align-items: center; justify-content: center;
  }
  .brand-name {
    writing-mode: vertical-rl;
    font-family: "Archivo Black", sans-serif;
    font-size: 15px; letter-spacing: 3px;
    color: var(--logo-text);
  }
  .sleeve {
    position: absolute; left: 170px; top: -2px;
    width: 815px; height: 644px;
  }
  .sleeve-pattern {
    position: absolute; inset: 0;
    background:
      radial-gradient(circle at 20% 20%, var(--pattern-light) 0, transparent 40%),
      radial-gradient(circle at 80% 80%, var(--pattern-deep) 0, transparent 55%),
      linear-gradient(135deg, #7f98aa 0%, var(--pattern-deep) 60%, #335d70 100%);
  }
  .info-panel {
    position: absolute; left: 58px; top: 100px;
    width: 700px; height: 440px;
    background: var(--panel-bg);
    border: 4px solid var(--panel-frame);
    overflow: hidden;
  }
  .dark-band {
    position: absolute; left: 0; right: 0; top: 233px; height: 132px;
    background: var(--band-dark);
  }
  .product-title {
    position: absolute; left: 0; right: 0; top: 24px;
    text-align: center;
    font-family: "Barlow Condensed", sans-serif;
    font-style: italic; font-weight: 600;
    font-size: 76px; line-height: 1;
    white-space: nowrap;
  }
  .product-title .word-light { color: var(--title-light); }
  .product-title .word-deep { color: var(--title-deep); }
  .mask-art {
    position: absolute; left: 170px; top: 120px;
    width: 320px; height: 280px;
    border-radius: 40px 40px 120px 60px;
    background: linear-gradient(160deg, #e4eff4 0%, var(--mask-fill) 70%);
  }
  .origin-badge {
    position: absolute; right: 38px; bottom: 22px;
    display: flex; align-items: center; gap: 5px;
  }
  .origin-badge .flag-block {
    width: 32px; height: 34px;
    background: linear-gradient(180deg, var(--badge-blue) 0 45%, var(--badge-red) 45% 100%);
  }
  .origin-badge .origin-text {
    display: flex; flex-direction: column;
    font-family: "Barlow Condensed", sans-serif; font-weight: 600;
    line-height: 0.9;
  }
  .origin-text .made-in { font-size: 12px; color: var(--badge-red); }
  .origin-text .country { font-size: 26px; color: var(--badge-blue); }
</style>
</head>
<body>
  <div class="box-front">
    <div class="brand-spine"><span class="brand-name">COMPANY LOGO</span></div>
    <div class="sleeve">
      <div class="sleeve-pattern" role="img" aria-label="Decorative pattern of cartoon viruses and microbes in blue and grey tones"></div>
      <div class="info-panel">
        <div class="dark-band"></div>
        <h1 class="product-title"><span class="word-light">DISPOSABLE</span> <span class="word-deep">FACE MASK</span></h1>
        <div class="mask-art" role="img" aria-label="Illustration of a light blue pleated disposable face mask with ear loops"></div>
        <div class="origin-badge">
          <span class="flag-block"></span>
          <span class="origin-text"><span class="made-in">MADE IN</span><span class="country">USA</span></span>
        </div>
      </div>
    </div>
  </div>
</body>
</html>
```